Tourism Brochure Design for a nature based eco retreat in Margaret River Western Australia

We need a new brochure as per the attached (a4 folded to DL) - would love a fresh nature inspired design which highlights the photos. Map would need to be reworked (simplified) to show we are close to town but in the National Park.

Text as per brochure mock up attached - copy maybe cut down if required to suit design.

Target Market(s)

Nature enthusiasts, families, bike riders, bush walkers

Industry/Entity Type

Town

Font styles to use
Sans Serif

Requirements
Must have
• Lots of nature, hand writing - not messy or too childish - but rustic. Local images (not ones from elsewhere). Font in logo is Higher than High - with the I modified as I dont like lower case mixed in with upper case! I dont love this font (but dont dislike it either!)
Should not have
• anything to american or clip art or polished looking (we are more rustic). Photos/images which are clearly not from here.

```html
<!DOCTYPE html>
<html lang="en">
<head>
<meta charset="utf-8">
<title>Bramblewood Hollow – Brochure</title>
<link rel="stylesheet" href="https://fonts.googleapis.com/css2?family=Amatic+SC:wght@700&family=Open+Sans:wght@400;600;700&display=swap">
<style>
:root{
  --forest:#35552a;
  --leaf:#8db43e;
  --lime:#b8d36a;
  --bark:#5a4a35;
  --ember:#c8452b;
  --paper:#ffffff;
  --mist:#eef3e4;
  --ink:#3a3a32;
}
*{box-sizing:border-box;margin:0;padding:0}
html,body{width:841px;height:1200px;overflow:hidden;background:#f2f2ee}
body{font-family:"Open Sans",Arial,sans-serif;color:var(--ink)}
.sheet{position:relative;width:841px;height:1200px}
.spread{position:absolute;left:0;width:841px;height:600px;background:var(--paper);display:flex}
.outside{top:0}
.inside{top:600px}
.panel{position:relative;width:280.3px;height:600px;overflow:hidden}
.panel+.panel{border-left:1px solid #e3e6dc}
.photo{position:absolute;left:0;width:100%}
.hand{font-family:"Amatic SC",cursive;font-weight:700;letter-spacing:.5px}

/* outside left */
.hero{top:0;height:165px;background:linear-gradient(160deg,#c9d8b8,#7e9a62 60%,#4f6b3b)}
.hero-line{position:absolute;left:18px;top:22px;width:200px;font-size:24px;line-height:1.02;color:var(--paper);text-transform:uppercase}
.features{position:absolute;left:0;top:165px;width:100%;height:140px;background:var(--lime);padding:14px 16px}
.features li{list-style:none;display:flex;gap:7px;font-size:11.5px;font-weight:700;color:var(--forest);line-height:1.25;margin-bottom:6px}
.features svg{flex:none;margin-top:2px}
.forest-view{top:305px;height:260px;background:linear-gradient(180deg,#5f7d48,#8d9b6a 45%,#c58a4a 85%,#6b5434)}
.footer-band{position:absolute;left:0;bottom:0;width:100%;height:35px;background:var(--forest);color:var(--paper);font-size:10px;font-weight:600;display:flex;align-items:center;padding-left:16px;letter-spacing:.3px}

/* outside middle */
.map{top:10px;height:300px;left:12px;width:256px;background:linear-gradient(135deg,#e7efdc,#cfe0b6);border:1px solid #b7c9a0}
.map-note{position:absolute;left:20px;top:322px;width:240px;font-size:8.5px;line-height:1.35;color:var(--bark);text-align:center}
.map-note b{display:block;font-size:9.5px;color:var(--forest)}
.mid-logo{position:absolute;left:80px;top:390px;width:120px;text-align:center}

/* logo */
.brand{display:flex;flex-direction:column;align-items:center;gap:5px;color:var(--forest);font-weight:700;text-transform:uppercase;letter-spacing:1px}
.brand .dot{width:46px;height:46px;border-radius:50%;background:var(--forest)}
.brand .name{font-size:15px;line-height:1.1}

/* outside right */
.cover-top{top:0;height:180px;background:linear-gradient(180deg,#eef3e4,#dfe9cf)}
.cover-logo{position:absolute;left:0;top:70px;width:100%}
.cover-logo .dot{width:58px;height:58px}
.cover-logo .name{font-size:20px}
.cover-photo{top:200px;height:285px;background:linear-gradient(170deg,#9fb07a,#5e7a43 50%,#3e5630)}
.contact{position:absolute;left:0;top:505px;width:100%;text-align:center;color:var(--forest)}
.contact .tel{font-size:19px;font-weight:700;letter-spacing:1px}
.contact .addr{font-size:9px;letter-spacing:1px;margin-top:4px;text-transform:uppercase}

/* inside */
.col{padding:16px 16px 0}
.head{background:var(--leaf);color:var(--paper);font-size:9.5px;font-weight:700;text-transform:uppercase;letter-spacing:.5px;padding:4px 8px;margin-bottom:7px}
.col p,.col li{font-size:8.4px;line-height:1.42;margin-bottom:5px}
.col ul{padding-left:11px}
.col b{color:var(--forest)}
.pics{position:absolute;left:16px;top:240px;width:248px;height:200px;display:grid;grid-template-columns:1fr 1fr;gap:5px}
.pics div{background:linear-gradient(160deg,#7e9a5e,#4a6537)}
.pics div:nth-child(2){background:linear-gradient(160deg,#b59b6e,#6b5a3c)}
.pics div:nth-child(3){grid-column:span 2;background:linear-gradient(160deg,#a6bb84,#5c7645)}
.tagline{position:absolute;left:0;top:470px;width:100%;display:flex;align-items:center;justify-content:center;gap:8px;font-size:30px;color:var(--leaf);text-transform:uppercase}
.band-light{position:absolute;left:0;bottom:0;width:100%;height:55px;background:var(--forest)}
.right-photo{position:absolute;left:16px;top:330px;width:248px;height:120px;background:linear-gradient(160deg,#d1c29b,#8a7650 60%,#4f6b3b)}
</style>
</head>
<body>
<div class="sheet">

  <!-- Outside spread -->
  <section class="spread outside">
    <div class="panel">
      <div class="photo hero" role="img" aria-label="Sunlit forest canopy photograph"></div>
      <p class="hero-line hand">Quintessentially Australian nature based experience in Margaret River which doesn't cost the earth</p>
      <ul class="features">
        <li><svg width="10" height="10" viewBox="0 0 10 10"><path d="M1 1L9 9M9 1L1 9" stroke="#c8452b" stroke-width="2.2"/></svg>Nestled in the forest – walk or ride to Margaret River town centre or the river</li>
        <li><svg width="10" height="10" viewBox="0 0 10 10"><path d="M1 1L9 9M9 1L1 9" stroke="#c8452b" stroke-width="2.2"/></svg>Rustic simplicity and loads of charm</li>
        <li><svg width="10" height="10" viewBox="0 0 10 10"><path d="M1 1L9 9M9 1L1 9" stroke="#c8452b" stroke-width="2.2"/></svg>Rustic style huts nestled with camp fires and a starlit sky</li>
      </ul>
      <div class="photo forest-view" role="img" aria-label="Tall karri forest with a warm glowing campfire"></div>
      <div class="footer-band">E: STAY@BRAMBLEWOODHOLLOW.COM.AU</div>
    </div>

    <div class="panel">
      <div class="photo map" role="img" aria-label="Simplified map showing the retreat in the national park close to town"></div>
      <p class="map-note"><b>Existing conditions</b>Just a short stroll from town along the river trail, tucked inside the national park. Easy access by foot or bike.</p>
      <div class="mid-logo brand"><span class="dot"></span><span class="name">Bramblewood Hollow</span></div>
      <div class="footer-band">WWW.BRAMBLEWOODHOLLOW.COM.AU</div>
    </div>

    <div class="panel">
      <div class="photo cover-top" role="img" aria-label="Soft pale forest light"></div>
      <div class="cover-logo brand"><span class="dot"></span><span class="name">Bramblewood Hollow</span></div>
      <div class="photo cover-photo" role="img" aria-label="Rustic timber hut among tall trees"></div>
      <div class="contact">
        <div class="tel">TEL: 08 9000 1234</div>
        <div class="addr">Fernleigh Road, Riverbend</div>
      </div>
      <div class="footer-band">WWW.BRAMBLEWOODHOLLOW.COM.AU</div>
    </div>
  </section>

  <!-- Inside spread -->
  <section class="spread inside">
    <div class="panel col">
      <div class="head">Situated in an amazing location</div>
      <p>The retreat sits on the edge of the national park, a short walk from the town centre and only minutes from the river and its sheltered swimming holes.</p>
      <p>Surrounded by tall trees, bird song and quiet walking trails, it is the perfect base for exploring caves, beaches, wineries and forest lookouts.</p>
      <p><b>Facilities:</b> shared kitchen, hot showers, fire pits, picnic tables, barbecues and free wifi in the common area.</p>
      <p><b>Onsite:</b> bike hire, walking maps, games room and a quiet library.</p>
      <div class="pics">
        <div role="img" aria-label="Forest walking track photograph"></div>
        <div role="img" aria-label="Timber hut interior photograph"></div>
        <div role="img" aria-label="Riverside trail photograph"></div>
      </div>
      <div class="tagline hand"><svg width="18" height="18" viewBox="0 0 18 18"><path d="M2 16C2 7 8 2 16 2C16 10 11 16 2 16Z" fill="#8db43e"/></svg>Bush walking</div>
      <div class="band-light"></div>
    </div>

    <div class="panel col">
      <div class="head">Simple eco accommodation</div>
      <ul>
        <li><b>Six rustic huts</b> each sleeping up to four guests, with a double bed, bunks and a small deck overlooking the bush.</li>
        <li><b>Two family cabins</b> with their own kitchenette, wood heater and outdoor bath under the trees.</li>
        <li><b>Camp sites</b> for tents and small vans, shaded and sheltered, with easy access to the amenities block.</li>
      </ul>
      <p>All lodgings are built from recycled timber and run on solar power, keeping our footprint light and our prices fair.</p>
      <p><b>Group stays</b> are welcome for schools, clubs and families. Ask us about weekly rates and bike packages.</p>
      <p>Linen, firewood and breakfast hampers are available on request.</p>
      <div class="pics">
        <div role="img" aria-label="Family cabin photograph"></div>
        <div role="img" aria-label="Camp fire photograph"></div>
        <div role="img" aria-label="Mountain trail photograph"></div>
      </div>
      <div class="tagline hand"><svg width="18" height="18" viewBox="0 0 18 18"><path d="M2 16C2 7 8 2 16 2C16 10 11 16 2 16Z" fill="#8db43e"/></svg>Mountain walking</div>
      <div class="band-light"></div>
    </div>

    <div class="panel col">
      <div class="head">Generating energy from the sun</div>
      <p>Our solar array provides most of the power used on site, with battery storage carrying us through the night.</p>
      <div class="head">Harvesting water</div>
      <p>Rain is collected from every roof and stored in large tanks, then filtered for drinking, washing and the gardens.</p>
      <div class="head">Interpretation nature &amp; culture</div>
      <p>The old timber mill and its surrounding forest tell a long story. Signs along the trail share local history, plants and wildlife.</p>
      <div class="right-photo" role="img" aria-label="Old timber mill building in the forest"></div>
      <div class="tagline hand"><svg width="18" height="18" viewBox="0 0 18 18"><path d="M2 16C2 7 8 2 16 2C16 10 11 16 2 16Z" fill="#8db43e"/></svg>Break amidst nature</div>
      <div class="band-light"></div>
    </div>
  </section>

</div>
</body>
</html>
```